- Talvisk
- Links to the website
- http://brelvomar.ca/
- Describe your company and organization and target audience
- Company secretarial and management for small business.
- The design should have the following
- The model should include :  - 5 pages. - Clean and modern design. - You must use the images are joined and make a mixture between the model of the website to respect and incorporate photos.
- Other Facts

```html
<!DOCTYPE html>
<html lang="en">
<head>
<meta charset="utf-8">
<title>Talvisk — Company Secretarial &amp; Management</title>
<link rel="stylesheet" href="https://fonts.googleapis.com/css2?family=Oswald:wght@300;400&family=Open+Sans:wght@400;600;700&family=Roboto:wght@400&display=swap">
<style>
:root{
  --blue:#0a4d8c;
  --blue-dark:#073b6d;
  --blue-band:#1f5f9c;
  --green:#6fb12b;
  --green-band:#72b02a;
  --grey-bg:#efefef;
  --ink:#333;
  --muted:#6a6a6a;
  --navy:#0e1a26;
  --white:#fff;
}
*{margin:0;padding:0;box-sizing:border-box}
html,body{width:743px;height:1200px;overflow:hidden;background:var(--white)}
body{position:relative;font-family:"Open Sans",Arial,sans-serif;color:var(--ink)}
.abs{position:absolute}

/* hero */
.hero{left:0;top:0;width:743px;height:351px;background:linear-gradient(160deg,#9aa3ad 0%,#cfd3d8 35%,#e6e3df 60%,#b9b2a8 100%)}
.call{right:109px;top:4px;font-size:7.5px;font-weight:700;color:var(--white);letter-spacing:.2px}
.brand{left:98px;top:18px;width:201px;height:35px;background:var(--green);display:flex;align-items:center;padding-left:14px;
  font-family:"Open Sans",sans-serif;font-weight:400;font-size:22px;letter-spacing:4px;color:var(--white);text-transform:uppercase}
.nav{left:299px;top:18px;width:338px;height:35px;background:var(--blue);display:flex;align-items:center;gap:17px;padding-left:32px;
  clip-path:polygon(0 0,100% 0,98% 100%,0 100%)}
.nav a{color:var(--white);font-size:7px;font-weight:700;text-decoration:none;text-transform:uppercase}
.tagline{left:172px;top:145px;width:399px;height:32px;background:#1b1b1b;color:var(--white);font-family:"Oswald",sans-serif;font-weight:400;
  font-size:23px;line-height:32px;text-align:center;letter-spacing:-.3px}
.circ-arrow{width:22px;height:22px}

/* feature boxes */
.feature{color:var(--white);text-align:center}
.feature h3{font-family:"Oswald",sans-serif;font-weight:300;font-size:16px;margin-top:8px;letter-spacing:.2px}
.feature p{font-size:6.4px;line-height:11.5px;margin-top:6px}
.f1{left:111px;top:317px;width:170px;height:138px;background:var(--blue);padding-top:16px}
.f2{left:281px;top:294px;width:183px;height:161px;background:var(--green);padding-top:40px}
.f3{left:464px;top:317px;width:168px;height:138px;background:var(--blue);padding-top:13px}

/* welcome */
.video{left:112px;top:491px;width:253px;height:126px;background:linear-gradient(135deg,#1c2a3a 0%,#3d4f63 50%,#8a6f5c 80%,#b3362e 100%)}
.play{left:214px;top:526px;width:44px;height:44px;border-radius:50%;background:rgba(255,255,255,.9)}
.welcome{left:377px;top:489px;width:253px}
.welcome h2{font-family:"Oswald",sans-serif;font-weight:300;font-size:17px;color:var(--blue);letter-spacing:-.2px}
.welcome p{font-size:7.7px;line-height:11.6px;color:var(--muted);text-align:justify;margin-top:4px}
.welcome p+p{margin-top:11px}
.btn{display:inline-block;background:var(--blue);color:var(--white);font-size:6.3px;font-weight:700;padding:4px 6px;text-decoration:none}
.welcome .btn{margin-top:9px}

/* statement band */
.band{left:0;top:642px;width:743px;height:73px;background:linear-gradient(100deg,#7cba31,#68a826 55%,#7ab82f);color:var(--white);
  font-family:"Roboto",sans-serif;font-size:18px;line-height:22px;text-align:center;padding-top:12px}

/* services */
.services{left:0;top:715px;width:743px;height:230px;background:var(--grey-bg)}
.card{top:736px;width:168px;height:187px;background:var(--white);border:1px solid #e0e0e0;border-bottom:2px solid var(--blue)}
.card .pic{position:absolute;left:9px;top:9px;width:149px;height:68px}
.card h4{position:absolute;left:10px;top:86px;font-size:9.2px;font-weight:700;color:var(--blue)}
.card p{position:absolute;left:10px;top:106px;width:148px;font-size:6.2px;line-height:10.5px;color:var(--muted);text-align:justify}
.card .btn{position:absolute;left:-1px;top:150px}

/* testimonials */
.testi{left:0;top:945px;width:743px;height:185px;background:linear-gradient(120deg,#1a568f,#22659f 50%,#1b5890)}
.quote{top:979px;width:252px;height:82px;background:var(--white);border-radius:3px;font-size:7.2px;line-height:11.8px;text-align:center;padding:20px 10px 0;color:#333}
.quote::after{content:"";position:absolute;left:18px;bottom:-7px;border:7px solid transparent;border-top-color:var(--white);border-bottom:0}
.avatar{width:40px;height:40px;border-radius:50%;background:linear-gradient(#d9d4cf,#a89f97);border:2px solid var(--white)}
.who{font-size:7.3px;line-height:11.5px;color:var(--white)}

/* footer */
.footer{left:0;top:1130px;width:743px;height:39px;background:var(--green-band)}
.mail{left:112px;top:1144px;font-size:7.3px;font-weight:700;color:var(--white);display:flex;align-items:center;gap:5px}
.social{top:1142px;width:13px;height:13px;border-radius:50%;background:var(--white)}
.legal{left:0;top:1169px;width:743px;height:31px;background:var(--navy);color:var(--white);font-size:6.5px;text-align:right;padding:14px 112px 0 0}
</style>
</head>
<body>

<header>
  <div class="abs hero" role="img" aria-label="Photo of business people at a meeting table with pens and a glass of water"></div>
  <div class="abs call">CALL US NOW : 0456-218-730</div>
  <div class="abs brand">Talvisk</div>
  <nav class="abs nav">
    <a href="http://brelvomar.ca/">Company</a>
    <a href="http://brelvomar.ca/">Incorporation</a>
    <a href="http://brelvomar.ca/">Accounting</a>
    <a href="http://brelvomar.ca/">Investment</a>
    <a href="http://brelvomar.ca/">Contact</a>
  </nav>
  <svg class="abs circ-arrow" style="left:112px;top:149px" viewBox="0 0 22 22"><circle cx="11" cy="11" r="9.5" fill="none" stroke="#111" stroke-width="2"/><path d="M13 6.5 8.5 11 13 15.5" fill="none" stroke="#111" stroke-width="2.2"/></svg>
  <h1 class="abs tagline">IDENTIFYING OPPORTUNITY. CREATING VALUE.</h1>
  <svg class="abs circ-arrow" style="left:609px;top:149px" viewBox="0 0 22 22"><circle cx="11" cy="11" r="9.5" fill="none" stroke="#111" stroke-width="2"/><path d="M9 6.5 13.5 11 9 15.5" fill="none" stroke="#111" stroke-width="2.2"/></svg>
</header>

<section>
  <div class="abs feature f1">
    <svg width="34" height="36" viewBox="0 0 34 36"><g fill="#fff"><rect x="2" y="24" width="5" height="11"/><rect x="10" y="19" width="5" height="16"/><rect x="18" y="14" width="5" height="21"/><rect x="26" y="9" width="5" height="26"/></g><path d="M2 19 12 9 18 14 30 2" fill="none" stroke="#fff" stroke-width="2.5"/><path d="M24 1h7v7" fill="none" stroke="#fff" stroke-width="2.5"/></svg>
    <h3>HEADING GOES HERE</h3>
    <p>Lorem ipsum dolor sit amet, consectetuer<br>adipiscing elit, sed diam nonummy nibh.</p>
  </div>
  <div class="abs feature f2">
    <svg width="44" height="32" viewBox="0 0 44 32"><g fill="#fff"><circle cx="17" cy="8" r="7"/><path d="M3 31c0-9 6-14 14-14s14 5 14 14z"/><circle cx="29" cy="10" r="6"/><path d="M24 31c2-7 5-12 8-12 6 0 10 5 10 12z"/></g></svg>
    <h3>HEADING GOES HERE</h3>
    <p>Lorem ipsum dolor sit amet, consectetuer<br>adipiscing elit, sed diam nonummy euismod.</p>
  </div>
  <div class="abs feature f3">
    <svg width="42" height="42" viewBox="0 0 42 42"><circle cx="21" cy="21" r="20" fill="#e9eef3"/><circle cx="21" cy="21" r="16" fill="#fff"/><path d="M21 11c-4 0-6 3-6 6 0 4 6 10 6 10s6-6 6-10c0-3-2-6-6-6z" fill="#e5533d"/><circle cx="21" cy="17" r="2.2" fill="#fff"/><circle cx="13" cy="25" r="2" fill="#e5533d"/><circle cx="29" cy="28" r="2" fill="#e5533d"/></svg>
    <h3>HEADING GOES HERE</h3>
    <p>Lorem ipsum dolor sit amet, consectetuer<br>adipiscing elit, sed nonummy nibh euismod.</p>
  </div>
</section>

<section>
  <div class="abs video" role="img" aria-label="Video still of a smiling man in front of a city skyline at dusk"></div>
  <svg class="abs play" viewBox="0 0 44 44"><path d="M18 14 30 22 18 30z" fill="var(--blue)"/></svg>
  <div class="abs welcome">
    <h2>WELCOME TO TALVISK</h2>
    <p>Lorem ipsum dolor sit amet, consectetuer adipiscing elit, sed diam nonummy nibh euismod tincidunt ut laoreet dolore magna aliquam erat volutpat. Ut wisi enim ad minim veniam, quis nostrud exerci tation. Lorem ipsum dolor sit amet.</p>
    <p>Sed diam nonummy nibh euismod tincidunt ut laoreet dolore magna aliquam erat volutpat.</p>
    <a class="btn" href="http://brelvomar.ca/">+ Read More</a>
  </div>
</section>

<div class="abs band">We establish and administer all forms of onshore and offshore<br>vehicles, including companies, partnerships and trusts.</div>

<section>
  <div class="abs services"></div>
  <svg class="abs circ-arrow" style="left:80px;top:809px" viewBox="0 0 22 22"><circle cx="11" cy="11" r="9.5" fill="none" stroke="var(--blue)" stroke-width="2"/><path d="M13 6.5 8.5 11 13 15.5" fill="none" stroke="var(--blue)" stroke-width="2.2"/></svg>
  <article class="abs card" style="left:111px">
    <div class="pic" role="img" aria-label="Photo of a presenter at a whiteboard with colleagues" style="background:linear-gradient(90deg,#d8d8d8,#f4f4f4 50%,#b5a89a)"></div>
    <h4>Heading Goes Here</h4>
    <p>Lorem ipsum dolor sit amet, suas ferri scribentur ea est. Qui in integre percipitur. In novum eligendi vis, an duis hendrerit quaerendum.</p>
    <a class="btn" href="http://brelvomar.ca/">+ Read More</a>
  </article>
  <article class="abs card" style="left:288px">
    <div class="pic" role="img" aria-label="Photo of a business handshake in front of a team" style="background:linear-gradient(180deg,#3a3d42,#6b6e73 60%,#9a9ca0)"></div>
    <h4>Heading Goes Here</h4>
    <p>Lorem ipsum dolor sit amet, suas ferri scribentur ea est. Qui in integre percipitur. In novum eligendi vis, an duis hendrerit quaerendum.</p>
    <a class="btn" href="http://brelvomar.ca/">+ Read More</a>
  </article>
  <article class="abs card" style="left:464px">
    <div class="pic" role="img" aria-label="Photo of hands on a keyboard beside a coffee cup" style="background:linear-gradient(135deg,#f2f2f2,#dcdcdc 55%,#4a4a4a)"></div>
    <h4>Heading Goes Here</h4>
    <p>Lorem ipsum dolor sit amet, suas ferri scribentur ea est. Qui in integre percipitur. In novum eligendi vis, an duis hendrerit quaerendum.</p>
    <a class="btn" href="http://brelvomar.ca/">+ Read More</a>
  </article>
  <svg class="abs circ-arrow" style="left:641px;top:809px" viewBox="0 0 22 22"><circle cx="11" cy="11" r="9.5" fill="none" stroke="var(--blue)" stroke-width="2"/><path d="M9 6.5 13.5 11 9 15.5" fill="none" stroke="var(--blue)" stroke-width="2.2"/></svg>
</section>

<section>
  <div class="abs testi"></div>
  <svg class="abs" style="left:145px;top:971px" width="190" height="98" viewBox="0 0 190 98"><path d="M14 0h189l-8 8H7z" fill="#10304f" transform="translate(-10 0)"/><path d="M8 90h170l-8 8H0z" fill="#10304f"/></svg>
  <svg class="abs" style="left:424px;top:971px" width="190" height="98" viewBox="0 0 190 98"><path d="M8 0h180l-8 8H0z" fill="var(--green)"/><path d="M8 90h170l-8 8H0z" fill="var(--green)"/></svg>
  <blockquote class="abs quote" style="left:113px">Lorem ipsum dolor sit amet, consectetuer adipiscing elit, sed diam nonummy nibh euismod tincidunt ut laoreet dolore magna aliquam erat volutpat. Ut wisi enim ad minim veniam, quis nostrud exerci tation.</blockquote>
  <blockquote class="abs quote" style="left:379px">Lorem ipsum dolor sit amet, consectetuer adipiscing elit, sed diam nonummy nibh euismod tincidunt ut laoreet dolore magna aliquam erat volutpat. Ut wisi enim ad minim veniam, quis nostrud exerci tation.</blockquote>
  <div class="abs avatar" style="left:113px;top:1074px" role="img" aria-label="Customer portrait photo"></div>
  <div class="abs who" style="left:158px;top:1082px">Customer Name<br>XYZ, Location</div>
  <div class="abs avatar" style="left:379px;top:1074px" role="img" aria-label="Customer portrait photo"></div>
  <div class="abs who" style="left:424px;top:1082px">Customer Name<br>XYZ, Location</div>
</section>

<footer>
  <div class="abs footer"></div>
  <div class="abs mail"><svg width="10" height="7" viewBox="0 0 10 7"><rect x=".5" y=".5" width="9" height="6" fill="none" stroke="#fff"/><path d="M.5.5 5 4 9.5.5" fill="none" stroke="#fff"/></svg>support@talvisk.com</div>
  <span class="abs social" style="left:544px"></span>
  <span class="abs social" style="left:568px"></span>
  <span class="abs social" style="left:592px"></span>
  <span class="abs social" style="left:618px"></span>
  <div class="abs legal">Copyright © 2016 Talvisk.&nbsp; All rights reserved.</div>
</footer>

</body>
</html>
```